I need bigcommerce design template

hi, am looking for a quality, professional, attractive and mature bigcommerce template for my site. My site will sell clothes and bags and shoes. Basically what you are to do is setup the store. I have domain name which nameharbor will attach them self.

```html
<!DOCTYPE html>
<html lang="en">
<head>
<meta charset="utf-8">
<title>Loomwell — Hazy Shade of Spring</title>
<link rel="stylesheet" href="https://fonts.googleapis.com/css2?family=Lato:wght@300;400;700&family=Lora:ital@1&display=swap">
<style>
:root{
  --page:#d8d8d8;--white:#fff;--ink:#2b2b2b;--muted:#666;--accent:#f08236;
  --tile-dark:#5a5a5a;--tile-light:#b4b4b4;--line:#dcdcdc;
}
*{box-sizing:border-box;margin:0;padding:0}
html,body{width:748px;height:1200px;overflow:hidden}
body{background:var(--page);font-family:"Lato",sans-serif;color:var(--ink);position:relative}
.hero{position:absolute;left:0;top:0;width:748px;height:322px;
  background:linear-gradient(160deg,#c9c2b4 0%,#e7dcc4 25%,#a99f86 50%,#6b6a4d 75%,#5b6438 100%)}
.nav{position:absolute;left:86px;top:10px;width:572px;height:38px;border-bottom:1px solid rgba(255,255,255,.35);font-size:7.5px;color:#333}
.brand{position:absolute;left:0;top:0;height:21px;padding:0 3px;background:#1d1d1d;color:#fff;font-size:7px;line-height:21px;letter-spacing:-.2px}
.nav a{position:absolute;top:6px;color:#333;text-decoration:none}
.nav svg{position:absolute;top:5px}
.hero h1{position:absolute;top:105px;width:100%;text-align:center;font-weight:400;font-size:34px;letter-spacing:1.6px;color:#2e2e2e}
.hero p{position:absolute;top:151px;width:100%;text-align:center;font-family:"Lora",serif;font-style:italic;font-size:13.5px;color:#222}
.btn{position:absolute;left:319px;top:197px;width:110px;height:28px;background:var(--accent);color:#fff;font-size:7px;text-align:center;line-height:28px;letter-spacing:.3px}
.panel{position:absolute;left:75px;top:322px;width:598px;height:840px;background:var(--white)}
.grid{position:absolute;left:16px;top:20px;display:grid;grid-template-columns:repeat(4,142px);grid-template-rows:repeat(3,142px)}
.tile{position:relative;display:flex;flex-direction:column;align-items:center;justify-content:center;text-align:center;color:#fff}
.tile h3{font-weight:700;font-size:12px;letter-spacing:.5px;line-height:13px}
.tile em{font-family:"Lora",serif;font-style:italic;font-size:9px;letter-spacing:.5px;text-transform:uppercase;margin-top:1px}
.dark{background:var(--tile-dark)}
.tweet{background:var(--tile-light);padding:0 22px}
.tweet p{font-family:"Lora",serif;font-style:italic;font-size:7px;line-height:9.5px;margin:9px 0 10px}
.tweet b{font-size:7px}
.mark{display:flex;align-items:center;gap:6px}
.mark i{width:10px;height:1px;background:#fff}
.mark span{width:10px;height:10px;border-radius:50%;background:#fff}
.arrow{font-size:14px;line-height:14px;margin-bottom:2px}
.signup{position:absolute;top:511px;width:100%;text-align:center}
.signup h2{font-weight:700;font-size:17.5px;letter-spacing:1px;color:#2d2d2d}
.signup p{font-family:"Lora",serif;font-style:italic;font-size:9.5px;color:#555;margin-top:5px}
.form{position:absolute;left:162px;top:572px;display:flex}
.form span{width:229px;height:27px;border:1px solid #bbb;font-family:"Lora",serif;font-style:italic;font-size:7px;color:#777;padding-left:7px;line-height:26px}
.form b{width:46px;height:27px;background:var(--accent);color:#fff;font-size:7px;font-weight:400;text-align:center;line-height:27px}
.carousel{position:absolute;left:16px;top:634px;width:569px;height:85px;display:flex}
.carousel .nav-arrow{width:18px;background:#e3e3e3;color:#fff;font-size:22px;display:flex;align-items:center;justify-content:center}
.carousel .item{flex:1}
.footer{position:absolute;left:16px;top:746px;display:flex}
.col{width:134px;padding-right:10px;font-size:6px;line-height:11px;color:#333}
.col+.col{width:144.5px;border-left:1px solid var(--line);padding-left:10px}
.col h4{font-size:7px;letter-spacing:.5px;margin-bottom:4px}
.col u{color:#333}
.socials{display:flex;gap:8px;margin-top:8px}
.socials span{width:15px;height:15px;border:1px solid #444}
</style>
</head>
<body>
<header class="hero" role="img" aria-label="Sunlit coastline with sea and green hills">
  <nav class="nav">
    <span class="brand">LOOMWELL</span>
    <a style="left:52px">Woman</a><a style="left:100px">Men</a><a style="left:138px">Kids</a>
    <a style="left:176px">Comming Soon</a><a style="left:248px">About</a>
    <svg style="left:432px" width="7" height="9" viewBox="0 0 7 9"><circle cx="3.5" cy="2.2" r="2" fill="#333"/><path d="M0 9 Q0 4.5 3.5 4.5 Q7 4.5 7 9Z" fill="#333"/></svg>
    <a style="left:442px">Log In</a>
    <svg style="left:484px" width="8" height="8" viewBox="0 0 8 8"><rect x="0" y="2" width="8" height="6" fill="#333"/><path d="M2.5 2 V1 H5.5 V2" stroke="#333" fill="none"/></svg>
    <a style="left:497px">Basket (0)</a>
    <svg style="left:557px" width="9" height="9" viewBox="0 0 9 9"><circle cx="3.5" cy="3.5" r="2.6" stroke="#444" fill="none" stroke-width="1.1"/><path d="M5.5 5.5 L8.5 8.5" stroke="#444" stroke-width="1.3"/></svg>
  </nav>
  <h1>HAZY SHADE OF SPRING</h1>
  <p>Quisque lorem tortor fringilla sed, vestibulum id, eleifend justo.</p>
  <span class="btn">CHECK NEW ARRIVALS</span>
</header>
<main class="panel">
  <section class="grid">
    <div class="tile" style="grid-row:span 2;background:linear-gradient(#bdb6ad,#8e8880)" role="img" aria-label="Man in grey waistcoat with leather bag">
      <h3 style="margin-top:-12px">HEATHER<br>GREY BASICS</h3><em>New arrival</em></div>
    <div class="tile tweet"><div class="mark"><i></i><span></span><i></i></div>
      <p>Opening Ceremony @NusaFashionWk tomorrow, FMers! Are you ready for the biggest fashion movement in</p><b>@AyuKirana</b></div>
    <div class="tile" style="background:linear-gradient(#e6e2dc,#c9b8a4)" role="img" aria-label="Pair of braided brown leather shoes"></div>
    <div class="tile dark"><span class="arrow">&larr;</span><h3>ELEGANT SHOES</h3><em>Braided leather</em></div>
    <div class="tile" style="background:linear-gradient(#6e7482,#4d5450)" role="img" aria-label="Green canvas sneakers"><h3 style="margin-top:-12px">CANVAS HIGHS</h3><em>$125.00</em></div>
    <div class="tile tweet"><div class="mark"><i></i><span></span><i></i></div>
      <p>Girls, Girls, Girls: A Look Back at 50 Years of the Torvale Calendar</p><b>@ModeDaily</b></div>
    <div class="tile" style="grid-row:span 2;background:linear-gradient(#7a6f6a,#4f5656)" role="img" aria-label="Woman in teal dress holding a handbag">
      <h3 style="margin-top:-4px">JEANS FOR<br>ADVENTURE</h3><em>New arrival</em></div>
    <div class="tile" style="background:linear-gradient(#b9b4ae,#7c6a5e)" role="img" aria-label="Man wearing a grey knit beanie"></div>
    <div class="tile dark"><span class="arrow">&larr;</span><h3>ROWAN HAT</h3><em>Beanie hat</em></div>
    <div class="tile" style="background:linear-gradient(#5c5955,#2f2e2d)" role="img" aria-label="Tweed blazer"><h3 style="margin-top:-10px">BASIC BLAZER</h3><em>From $499.00</em></div>
  </section>
  <section class="signup">
    <h2>SIGN UP TO RECEIVE OUR UPDATES</h2>
    <p>Nulla ipsum dolor lacus, suscipit adipiscing. Cum sociis natoque penatibus et ultrices volutpat.</p>
  </section>
  <div class="form"><span>Your e-mail</span><b>add</b></div>
  <section class="carousel">
    <span class="nav-arrow">&#8249;</span>
    <span class="item" style="background:#6a5040" role="img" aria-label="Brown shoes"></span>
    <span class="item" style="background:#3a3531" role="img" aria-label="Leather jacket"></span>
    <span class="item" style="background:#5b3f36" role="img" aria-label="Leather gloves"></span>
    <span class="item" style="background:#b08b84" role="img" aria-label="Pink handbag"></span>
    <span class="item" style="background:#4a4d55" role="img" aria-label="Dark leather boots"></span>
    <span class="item" style="background:#cfcac5" role="img" aria-label="High heel shoe"></span>
    <span class="nav-arrow">&#8250;</span>
  </section>
  <footer class="footer">
    <div class="col"><h4>COLLECTION</h4><u>Woman (1725)</u><br>Men (635)<br>Kids (2514)<br>Comming Soon (76)</div>
    <div class="col"><h4>SITE</h4>Terms of Service<br>Privacy Policy<br>Copyright Policy<br>Press Kit<br>Support</div>
    <div class="col"><h4>SHOP</h4>About us<br>Shipping Metods<br>Career<br>Contact</div>
    <div class="col"><h4>SOCIAL</h4>Loomwell is made with love in Warsaw,<br>2014 © All rights reserved. Brightfold
      <div class="socials"><span></span><span></span><span></span></div></div>
  </footer>
</main>
</body>
</html>
```